Alloy wheel repair business needs a website

Install logo previously purchased from vantoquill, toolbar with dropdowns. services, gallery, clients , contact ect
Maybe mission statment

Target Market(s)

vehicle owners, auto dealers,insurance companies,

Industry/Entity Type

Alloy Wheel Repair

Coding

Coded - Design and coding required

Number of Pages Required

4 page

Font styles to use
Sans Serif

Colors
0054AA
0677BA
7BADD7
CADEEF
E8F1F8

```html
<!DOCTYPE html>
<html lang="en">
<head>
<meta charset="utf-8">
<title>Rimora Wheels – Alloy Wheel Repair</title>
<link href="https://fonts.googleapis.com/css2?family=Josefin+Sans:wght@700&family=Poppins:wght@400;500;600;700&display=swap" rel="stylesheet">
<style>
:root{
  --blue-deep:#0054AA;
  --blue:#0677BA;
  --blue-band:#0a74c9;
  --blue-soft:#7BADD7;
  --blue-pale:#CADEEF;
  --blue-mist:#E8F1F8;
  --ink:#222;
  --grey:#555;
  --black:#000;
  --white:#fff;
}
*{box-sizing:border-box;margin:0;padding:0}
html,body{width:1200px;height:4307px;overflow:hidden;background:var(--white)}
body{position:relative;font-family:"Poppins",sans-serif;color:var(--ink)}
.abs{position:absolute}
.display{font-family:"Josefin Sans",sans-serif;font-weight:700}
.ph{position:absolute}
/* nav */
.brand{display:flex;align-items:center;gap:10px;color:var(--blue);font-weight:700;font-size:30px;letter-spacing:2px}
.brand .dot{width:26px;height:26px;border-radius:50%;background:var(--blue)}
.nav{left:561px;top:56px;width:547px;display:flex;justify-content:space-between;font-size:15px;color:var(--blue)}
/* hero */
.hero{left:0;top:130px;width:1200px;height:595px;background:linear-gradient(180deg,#4a4f55,#2a2d31 60%,#1f2226)}
.hero-title{left:0;top:212px;width:1200px;text-align:center;color:var(--white);font-size:60px;line-height:68px}
.hero-text{left:260px;top:380px;width:680px;text-align:center;color:var(--white);font-size:18px;line-height:27px;font-weight:500}
.btn-light{left:516px;top:495px;width:168px;height:43px;background:var(--white);color:var(--ink);font-size:17px;display:flex;align-items:center;justify-content:center}
.feature{width:317px;height:242px;background:var(--white);top:625px}
.feature .ph{left:13px;top:12px;right:13px;bottom:12px}
.feature-label{top:878px;width:317px;text-align:center;font-size:19px;font-weight:500;color:#444}
/* headings */
.section-title{left:0;width:1200px;text-align:center;color:var(--blue);font-size:54px}
.smallcaps{font-variant:small-caps}
/* services */
.service{top:1103px;width:314px;height:343px;border:1.5px solid var(--blue-soft);text-align:center}
.service .icon{width:86px;height:86px;border-radius:50%;background:var(--blue);margin:32px auto 0;display:flex;align-items:center;justify-content:center}
.service h3{margin-top:22px;font-size:26px;font-weight:500;color:var(--blue)}
.service p{margin:30px auto 0;width:240px;font-size:18px;line-height:27px;color:var(--grey)}
/* about */
.about{left:0;top:1539px;width:1200px;height:440px;background:var(--blue-band)}
.about h2{left:154px;top:1605px;color:var(--white);font-size:54px}
.about-text{left:154px;top:1690px;width:390px;color:var(--white);font-size:21px;line-height:24px;font-weight:500}
.btn-outline{left:149px;top:1862px;width:157px;height:43px;border:1.5px solid var(--white);border-radius:22px;color:var(--white);font-size:17px;display:flex;align-items:center;justify-content:center}
/* clients */
.arrow{width:64px;height:64px;border-radius:50%;background:var(--blue);top:3181px}
.client{top:3188px;font-size:34px;font-weight:700;color:var(--black);text-align:center;width:200px}
/* contact */
.contact{left:0;top:3334px;width:1200px;height:566px;background:var(--black)}
.field{border-bottom:2px solid #cfcfcf;color:#ddd;font-size:17px;padding-bottom:12px}
.btn-quote{left:192px;top:3776px;width:341px;height:57px;background:var(--blue-band);color:var(--white);font-size:18px;font-weight:600;display:flex;align-items:center;justify-content:center}
.logo-box{left:784px;top:3522px;width:270px;height:116px;background:var(--white);display:flex;align-items:center;justify-content:center}
.social-dot{width:20px;height:20px;border-radius:50%;background:var(--white)}
/* footer */
.foot-h{top:3965px;font-size:20px;font-weight:500;color:var(--blue)}
.foot-list{list-style:none;font-size:20px;line-height:34.5px;color:#333}
.foot-list li::before{content:"› ";color:var(--blue)}
.foot-contact{left:820px;top:4025px;font-size:18px;color:#333}
.foot-contact div{display:flex;gap:12px;margin-bottom:10px;line-height:24px}
.foot-dot{width:22px;height:22px;border-radius:50%}
.copyright{left:0;top:4201px;width:1200px;height:106px;background:#f1f1f1;border-top:1px solid #ddd;text-align:center;padding-top:26px;font-size:18px;font-weight:500}
</style>
</head>
<body>

<!-- Header -->
<div class="abs brand" style="left:105px;top:48px"><span class="dot"></span>RIMORA</div>
<nav class="abs nav"><span>HOME</span><span>ABOUT US</span><span>SERVICES</span><span>GALLERY</span><span>CLIENTS</span><span>CONTACT</span></nav>

<!-- Hero -->
<div class="abs hero" role="img" aria-label="Dark sports car parked by a harbour at dusk"></div>
<h1 class="abs display hero-title">MOST EXCLUSIVE AND<br>VARITIES OF ALLOYS</h1>
<p class="abs hero-text">Lorem ipsum dolor sit amet, consectetur adipiscing elit, sed do eiusmod tempor incididunt ut labore et dolore magna aliqua. Quis ipsum suspendisse ultrices gravida.</p>
<div class="abs btn-light">Read More</div>

<div class="abs feature" style="left:89px"><div class="ph" role="img" aria-label="Close-up of a silver multi-spoke alloy wheel with red brake caliper" style="background:linear-gradient(135deg,#8a8d92,#3a3c40)"></div></div>
<div class="abs feature" style="left:441px"><div class="ph" role="img" aria-label="Grey car with bronze alloy wheel" style="background:linear-gradient(135deg,#9aa3ad,#4a5058)"></div></div>
<div class="abs feature" style="left:794px"><div class="ph" role="img" aria-label="Mechanic cleaning the wheel of a yellow-black sports car" style="background:linear-gradient(135deg,#7d8a7a,#2f3a2c 60%,#a9b84a)"></div></div>
<div class="abs feature-label" style="left:89px">ALLOY WORKS</div>
<div class="abs feature-label" style="left:441px">NEW ALLOYS</div>
<div class="abs feature-label" style="left:794px">HIGH QUALITY</div>

<!-- Services -->
<h2 class="abs display section-title" style="top:1005px">OUR SERVICES</h2>
<div class="abs service" style="left:80px">
  <div class="icon"><svg width="40" height="40" viewBox="0 0 40 40"><circle cx="20" cy="20" r="9" fill="none" stroke="#fff" stroke-width="4" stroke-dasharray="5 3"/><circle cx="20" cy="20" r="3" fill="#fff"/></svg></div>
  <h3>Premium Care</h3>
  <p>We give every customer our bestavailable rate every time.</p>
</div>
<div class="abs service" style="left:438px">
  <div class="icon"><svg width="40" height="40" viewBox="0 0 40 40"><rect x="7" y="13" width="26" height="18" rx="2" fill="#fff"/><rect x="15" y="8" width="10" height="6" fill="none" stroke="#fff" stroke-width="3"/><rect x="7" y="20" width="26" height="2" fill="#0677BA"/></svg></div>
  <h3>Budget Friendly</h3>
  <p>We've made our process quick andeasy to get you funded faster.</p>
</div>
<div class="abs service" style="left:795px">
  <div class="icon"><svg width="44" height="44" viewBox="0 0 44 44"><circle cx="22" cy="22" r="16" fill="none" stroke="#fff" stroke-width="3"/><circle cx="22" cy="22" r="9" fill="none" stroke="#fff" stroke-width="3"/><circle cx="22" cy="22" r="3" fill="#fff"/></svg></div>
  <h3>Power Ratio</h3>
  <p>From good to bad credit, we havea program that fits your business</p>
</div>

<!-- About -->
<section class="abs about"></section>
<h2 class="abs display" style="left:154px;top:1605px;color:var(--white);font-size:54px">ABOUT US</h2>
<p class="abs about-text">Lorem ipsum dolor sit amet, consectetur adipiscing elit, sed do eiusmod tempor incididunt ut labore et dolore magna aliqua. Quis ipsum dolore magna aliqua</p>
<div class="abs btn-outline">Read More</div>
<div class="abs" role="img" aria-label="Orange sports car by a stormy sea" style="left:662px;top:1571px;width:388px;height:388px;border-radius:50%;background:linear-gradient(180deg,#9aa2aa,#6f7780 50%,#d5581f 52%,#3b3b3b)"></div>

<!-- Gallery -->
<h2 class="abs display section-title" style="top:2093px">OUR GALLERY</h2>
<div class="ph" role="img" aria-label="Black alloy wheel with orange brake caliper" style="left:79px;top:2197px;width:264px;height:246px;background:linear-gradient(135deg,#3a3a3a,#1a1a1a)"></div>
<div class="ph" role="img" aria-label="Grey car side with silver wheel" style="left:371px;top:2197px;width:262px;height:246px;background:linear-gradient(135deg,#8e959c,#4b5157)"></div>
<div class="ph" role="img" aria-label="Blue car with black alloy wheel" style="left:662px;top:2197px;width:461px;height:246px;background:linear-gradient(135deg,#1d2f7a,#2a2c33 60%,#bfc3c8)"></div>
<div class="ph" role="img" aria-label="White car with black wheel and red caliper" style="left:79px;top:2480px;width:462px;height:246px;background:linear-gradient(135deg,#d8d8d8,#2b2b2b 50%,#cfcfcf)"></div>
<div class="ph" role="img" aria-label="Tyre with white classic rim" style="left:570px;top:2480px;width:262px;height:246px;background:radial-gradient(circle,#e8e8e8 30%,#1a1a1a 60%,#000)"></div>
<div class="ph" role="img" aria-label="Blue car with silver sport wheel" style="left:861px;top:2480px;width:264px;height:246px;background:linear-gradient(135deg,#e6e8ec,#2540a8 45%,#5a5e66)"></div>
<div class="ph" role="img" aria-label="Black alloy wheel with orange brake caliper" style="left:79px;top:2762px;width:264px;height:246px;background:linear-gradient(135deg,#3a3a3a,#1a1a1a)"></div>
<div class="ph" role="img" aria-label="Mechanic cleaning the wheel of a yellow-black sports car" style="left:371px;top:2762px;width:461px;height:246px;background:linear-gradient(135deg,#7d8a7a,#2f3a2c 60%,#a9b84a)"></div>
<div class="ph" role="img" aria-label="Technician fitting a silver wheel" style="left:861px;top:2762px;width:264px;height:246px;background:linear-gradient(135deg,#24356e,#b8bcc2)"></div>

<!-- Clients -->
<h2 class="abs display smallcaps section-title" style="top:3072px;font-size:54px">Our Clients</h2>
<div class="abs arrow" style="left:95px"><svg width="64" height="64" viewBox="0 0 64 64"><path d="M37 22 L27 32 L37 42" fill="none" stroke="#fff" stroke-width="5"/></svg></div>
<div class="abs arrow" style="left:1034px"><svg width="64" height="64" viewBox="0 0 64 64"><path d="M27 22 L37 32 L27 42" fill="none" stroke="#fff" stroke-width="5"/></svg></div>
<div class="abs client" style="left:181px;font-size:24px;line-height:24px;top:3192px">Northgate<br>Weekly</div>
<div class="abs client" style="left:385px">TQJ</div>
<div class="abs client" style="left:599px;font-size:48px;top:3180px">KELT.</div>
<div class="abs client" style="left:832px">VRNews</div>

<!-- Contact -->
<section class="abs contact"></section>
<h2 class="abs display smallcaps" style="left:185px;top:3370px;color:var(--blue);font-size:54px">Contact us</h2>
<div class="abs field" style="left:192px;top:3478px;width:481px">Enter &nbsp;Name</div>
<div class="abs field" style="left:192px;top:3547px;width:237px">Enter Your Name</div>
<div class="abs field" style="left:455px;top:3547px;width:215px">Enter Phone number</div>
<div class="abs field" style="left:192px;top:3615px;width:481px">&nbsp;Enter Your Address</div>
<div class="abs field" style="left:192px;top:3684px;width:481px">Enter Your Email</div>
<div class="abs btn-quote">Get Instant Quote</div>
<div class="abs logo-box"><div class="brand"><span class="dot"></span>RIMORA</div></div>
<div class="abs social-dot" style="left:847px;top:3680px"></div>
<div class="abs social-dot" style="left:891px;top:3680px"></div>
<div class="abs social-dot" style="left:934px;top:3680px"></div>
<div class="abs social-dot" style="left:976px;top:3680px"></div>

<!-- Footer -->
<div class="abs brand" style="left:95px;top:4036px;font-size:24px"><span class="dot" style="width:20px;height:20px"></span>RIMORA</div>
<div class="abs foot-dot" style="left:113px;top:4102px;background:#c2187a"></div>
<div class="abs foot-dot" style="left:151px;top:4102px;background:#1d9bf0"></div>
<div class="abs foot-dot" style="left:188px;top:4102px;background:#3b5a9a"></div>

<div class="abs foot-h" style="left:276px">Quick Links</div>
<ul class="abs foot-list" style="left:276px;top:4022px"><li>About</li><li>Services</li><li>Contact</li><li>Home</li></ul>
<div class="abs foot-h" style="left:526px">Information</div>
<ul class="abs foot-list" style="left:526px;top:4022px"><li>Terms &amp; Condition</li><li>Privacy Policy</li><li>About Us</li><li>Support</li></ul>
<div class="abs foot-h" style="left:820px">Contact Us</div>
<div class="abs foot-contact">
  <div><svg width="22" height="24" viewBox="0 0 22 24"><path d="M5 2 L9 7 L7 10 Q9 15 13 17 L16 15 L20 19 L17 22 Q6 20 2 6 Z" fill="#0677BA"/></svg>555-014-2290</div>
  <div><svg width="22" height="24" viewBox="0 0 22 24"><rect x="1" y="6" width="20" height="14" fill="none" stroke="#0677BA" stroke-width="2"/><path d="M1 6 L11 14 L21 6" fill="none" stroke="#0677BA" stroke-width="2"/></svg>hello@rimorawheels.example</div>
  <div><svg width="22" height="28" viewBox="0 0 22 28"><path d="M11 1 C4 1 2 7 4 11 L11 26 L18 11 C20 7 18 1 11 1Z" fill="#0677BA"/><circle cx="11" cy="9" r="3" fill="#fff"/></svg><span>Lorem ipsum dolor sit amet,<br>consectetur &nbsp;dolor sit amet</span></div>
</div>

<div class="abs copyright">All rights reserved.Copyrights @ 2023</div>

</body>
</html>
```